Flyer-Design für IT Firma
Zielgruppe
Wir sind eine IT Firma aus München und möchten unsere Dienstleistung vermarkten. Unsere Zielgruppe sind hauptsächlich Endkunden und kleinere Firmen.
Aufgabenstellung
Ich habe mal einen Flyer gesehen der ebenfalls IT Dienstleistung beworben hat und in Kachelform mit kleinen Icons zu den Dienstleistungen aufgebaut war. War ganz schön aber ist nicht zwingend. Gerne lassen wir uns von neuen Vorschlägen überraschen.
Format war A6 Doppelseitig angedacht. Falls sich ein anderes Format besser eignet sind wir auch dafür offen.
Den Inhalt habe ich als Word Datei hoch geladen.
Das Logo habe ich leider nicht als EI oder APS Datei, und somit auch nur als Word Datei hoch geladen. Jedes Element ist aber einzeln bearbeitbar. Falls in Verbindung mit dem Flyer Design eine leichte Modernisierung des Logos notwendig ist, wäre das kein Problem.

```html
<!DOCTYPE html>
<html lang="de">
<head>
<meta charset="utf-8">
<title>VEKTA – Faltblatt 6-seitig, Wickelfalz</title>
<link href="https://fonts.googleapis.com/css2?family=Archivo+Black&family=Arimo:wght@400;700&family=Ubuntu:wght@400;500&display=swap" rel="stylesheet">
<style>
  :root{
    --blue:#0a6cc2;
    --blue-deep:#0b5fb0;
    --ink:#141414;
    --ink-soft:#1f1f1f;
    --paper:#ffffff;
    --stage:#dcdcdc;
    --text:#2a2a2a;
    --muted:#555;
  }
  *{box-sizing:border-box;margin:0;padding:0}
  html,body{width:1200px;height:2626px;overflow:hidden}
  body{
    position:relative;
    background:radial-gradient(ellipse at 50% 30%,#ececec 0%,var(--stage) 60%,#cfcfcf 100%);
    font-family:"Arimo",Arial,sans-serif;
    color:var(--text);
  }
  .panel{position:absolute;width:380px;height:380px;overflow:hidden;background:var(--paper)}
  .panel > svg.bg{position:absolute;left:0;top:0;width:380px;height:380px}
  .abs{position:absolute}
  .head-black{font-family:"Archivo Black",sans-serif;color:#fff;line-height:.92;text-transform:uppercase}
  .brand{font-family:"Archivo Black",sans-serif;color:#fff;letter-spacing:1px}
  .small{font-size:7px;line-height:1.35}
  .tiny{font-size:6.3px;line-height:1.35}
  .white{color:#fff}
  .bold{font-weight:700}

  .cover{left:277px;top:100px;transform:scale(1.7);transform-origin:0 0;box-shadow:0 8px 30px rgba(0,0,0,.25)}

  .banner{position:absolute;left:0;top:898px;width:1200px;height:134px;background:var(--blue);color:#fff;font-family:"Ubuntu",sans-serif}
  .banner .line1{position:absolute;left:78px;top:8px;white-space:nowrap}
  .banner .big{font-size:60px;font-weight:500}
  .banner .rest{font-size:40px;margin-left:10px}
  .banner .line2{position:absolute;left:78px;top:78px;font-size:40px}

  .spread{position:absolute;left:30px;width:1140px;height:380px;box-shadow:0 10px 30px rgba(0,0,0,.22)}
  .spread .panel{top:0}
  .p1{left:0}.p2{left:380px}.p3{left:760px}
  .outside{top:1130px}
  .inside{top:2000px}
  .caption{position:absolute;left:0;width:1200px;text-align:center;font-family:"Ubuntu",sans-serif;font-size:40px;color:#222}

  .blue-head{font-family:"Arimo",sans-serif;color:var(--blue);font-size:17px;line-height:1;text-transform:uppercase}
  .dark-head{color:var(--ink)}
  .icon{position:absolute;width:22px;height:22px}
</style>
</head>
<body>

<div class="panel cover">
  <svg class="bg" viewBox="0 0 380 380">
    <defs>
      <linearGradient id="bulbA" x1="0" y1="0" x2="1" y2="1">
        <stop offset="0" stop-color="#2a2a2a"/><stop offset=".35" stop-color="#1aa59a"/>
        <stop offset=".6" stop-color="#0b5fe0"/><stop offset="1" stop-color="#1c1c1c"/>
      </linearGradient>
    </defs>
    <rect width="380" height="380" fill="var(--ink)"/>
    <polygon points="80,55 380,0 380,215 165,275 80,275" fill="url(#bulbA)" role="img" aria-label="Foto: Hand hält leuchtende Glühbirne unter einem Haus-Symbol"/>
    <polygon points="220,0 380,0 380,25 245,75" fill="var(--ink-soft)"/>
    <polygon points="0,190 160,145 160,258 0,292" fill="var(--ink)"/>
    <polygon points="0,300 172,277 285,380 0,380" fill="#1c1c1c"/>
    <polygon points="192,276 380,216 380,380 302,380" fill="var(--blue)"/>
    <polygon points="172,276 188,275 298,380 282,380" fill="#fff"/>
  </svg>
  <div class="abs bold white" style="left:262px;top:30px;font-size:9px;transform:rotate(-12deg)">seit über 20 Jahren</div>
  <div class="abs head-black" style="left:20px;top:200px;font-size:19px">Lokaler<br>Computer<br>Service</div>
  <div class="abs brand" style="left:285px;top:318px;font-size:24px">VEKTA</div>
  <div class="abs white" style="left:24px;top:338px;font-size:7.5px;line-height:1.4">Ihr zuverlässiger Partner<br>für Hard- &amp; Software Produkte und<br>IT &amp; EDV Dienstleistung in München</div>
</div>

<div class="banner">
  <div class="line1"><span class="big">faltblatt</span><span class="rest">gefalzt auf quadrat 10.0 cm x 10.0 cm</span></div>
  <div class="line2">6-seiter (wickelfalz)</div>
</div>

<div class="spread outside">
  <div class="panel p1">
    <svg class="bg" viewBox="0 0 380 380">
      <polygon points="0,0 380,0 380,265 0,175" fill="#8a8a8a" role="img" aria-label="Schwarzweißfoto: Beratungsgespräch am Laptop"/>
      <polygon points="0,130 170,105 170,225 0,250" fill="var(--blue)"/>
    </svg>
    <div class="abs head-black" style="left:26px;top:138px;font-size:22px">Beratung<br>Computer<br>Service</div>
    <div class="abs bold" style="left:32px;top:262px;font-size:8px">Kaufberatung</div>
    <div class="abs small" style="left:32px;top:276px;width:325px">Ihre Wünsche stehen bei der Beratung im Vordergrund. Gemeinsam finden wir das richtige Angebot! Sie bekommen eine kompetente Beratung zu allen Produkten gängiger IT-Hersteller und bei der geplanten Einrichtung von Heim- &amp; Firmennetzwerken.<br>Nach dem Kauf stehen wir Ihnen selbstverständlich weiterhin zur Seite. Wir verkaufen eigens geprüfte Desktop-, Business- und Gaming-PC's. Wir bieten Hilfe bei Problemen mit E-Mail-Programmen und Providern.<br>Datenübernahme, Sicherung vorhandener Daten auf externe Hardware. Im IT-Bereich sind wir Ihr Fachmann.</div>
    <svg class="icon" style="left:345px;top:350px;width:20px;height:20px" viewBox="0 0 24 24" fill="none" stroke="var(--blue)" stroke-width="2.2"><rect x="2" y="10" width="11" height="6" rx="3" transform="rotate(-45 7.5 13)"/><rect x="11" y="8" width="11" height="6" rx="3" transform="rotate(-45 16.5 11)"/></svg>
  </div>

  <div class="panel p2">
    <svg class="bg" viewBox="0 0 380 380">
      <rect width="380" height="380" fill="var(--ink)"/>
      <polygon points="0,45 285,45 360,135 0,240" fill="#fff"/>
      <polygon points="190,380 380,318 380,324 205,380" fill="#fff"/>
    </svg>
    <div class="abs brand" style="left:0;width:380px;text-align:center;top:225px;font-size:26px">VEKTA</div>
    <div class="abs white tiny" style="left:18px;top:312px">VEKTA Handels GmbH<br>Lindenhofstr. 12<br>80331 München</div>
    <div class="abs white tiny" style="left:255px;top:318px">Tel.: 089 / 555 20 40<br>E-Mail: info@vekta.de</div>
  </div>

  <div class="panel p3">
    <svg class="bg" viewBox="0 0 380 380">
      <defs>
        <linearGradient id="bulbB" x1="0" y1="0" x2="1" y2="1">
          <stop offset="0" stop-color="#2a2a2a"/><stop offset=".35" stop-color="#1aa59a"/>
          <stop offset=".6" stop-color="#0b5fe0"/><stop offset="1" stop-color="#1c1c1c"/>
        </linearGradient>
      </defs>
      <rect width="380" height="380" fill="var(--ink)"/>
      <polygon points="80,55 380,0 380,215 165,275 80,275" fill="url(#bulbB)" role="img" aria-label="Foto: Hand hält leuchtende Glühbirne unter einem Haus-Symbol"/>
      <polygon points="220,0 380,0 380,25 245,75" fill="var(--ink-soft)"/>
      <polygon points="0,190 160,145 160,258 0,292" fill="var(--ink)"/>
      <polygon points="0,300 172,277 285,380 0,380" fill="#1c1c1c"/>
      <polygon points="192,276 380,216 380,380 302,380" fill="var(--blue)"/>
      <polygon points="172,276 188,275 298,380 282,380" fill="#fff"/>
    </svg>
    <div class="abs bold white" style="left:245px;top:32px;font-size:9px;transform:rotate(-8deg)">seit über 20 Jahren</div>
    <div class="abs head-black" style="left:20px;top:200px;font-size:19px">Lokaler<br>Computer<br>Service</div>
    <div class="abs brand" style="left:275px;top:312px;font-size:22px">VEKTA</div>
    <div class="abs white tiny" style="left:22px;top:338px">Ihr zuverlässiger Partner<br>für Hard- &amp; Software Produkte und<br>IT &amp; EDV Dienstleistung in München</div>
  </div>
</div>
<div class="caption" style="top:1588px">Flyer Außen geöffnet</div>

<div class="spread inside">
  <div class="panel p1">
    <svg class="bg" viewBox="0 0 380 380">
      <polygon points="0,0 380,20 380,60 195,262 0,238" fill="#7b7b7b" role="img" aria-label="Schwarzweißfoto: Handschlag zweier Geschäftsleute"/>
      <polygon points="0,120 180,95 180,210 0,232" fill="var(--blue)"/>
    </svg>
    <div class="abs" style="left:18px;top:128px;font-size:19px;line-height:.95;color:#fff;text-transform:uppercase">Ihr<br>Partner bei<br>IT-Sicherheit</div>
    <div class="abs bold" style="left:20px;top:250px;font-size:7.5px">IT-Sicherheitspartner</div>
    <div class="abs tiny" style="left:20px;top:262px;width:160px">Seit über 20 Jahren bauen wir Ihre Netzwerke und Serversysteme auf und das mit Leidenschaft.<br>Unsere Kernkompetenzen haben wir im Tausch von Hard- &amp; Software um Performance auf alten Systemen zu erhöhen, Umstellungen oder Störungsbehebungen, Installation von Betriebssystemen, Treiberinstallation und individuell gewünschter Software, Installieren vorhandener Geräte wie Drucker, Scanner, Kameras etc.</div>
    <div class="abs tiny" style="left:215px;top:318px;width:130px">Im Rahmen unserer Serverbetreuung ist eine moderne IT-Sicherheit für Ihr Unternehmen eine absolute Selbstverständlichkeit.</div>
    <svg class="icon" style="left:328px;top:338px;width:34px;height:30px" viewBox="0 0 34 30"><circle cx="9" cy="6" r="4" fill="var(--blue)"/><path d="M3 29 L8 12 L13 12 L16 29 Z" fill="var(--blue)"/><path d="M20 8 L32 11 C32 20 28 26 24 29 C20 26 17 20 17 11 Z" fill="var(--ink)"/></svg>
  </div>

  <div class="panel p2">
    <svg class="bg" viewBox="0 0 380 380">
      <polygon points="30,45 355,45 345,170 0,150" fill="var(--blue)"/>
      <rect x="30" y="290" width="150" height="85" fill="#2b2b2b" stroke="var(--blue)" stroke-width="2" role="img" aria-label="Foto: Hand mit Glühbirnen-Symbol"/>
    </svg>
    <div class="abs bold white" style="left:38px;top:52px;font-size:7px">IT-Securitylösungen</div>
    <div class="abs white tiny" style="left:38px;top:63px;width:300px">Wasserdichte und ganzheitliche IT-Securitylösungen bieten wir in unserem Paket IT-Security an. Entfernung vorhandener Schadsoftware und Bereinigung des Betriebssystems und bei der Konfiguration von Internetanschlüssen, bieten wir vor-Ort Hilfe &amp; sind wir Ihr zuverlässiger Partner. Wir versorgen Unternehmen mit topaktuellen Endpunkt-Sicherheits-Lösungen und entwickeln ein lupenreines Identitäts- und Passwortmanagement.</div>
    <div class="abs blue-head" style="left:35px;top:195px">Smarte<br><span class="dark-head">Lösungen</span><br>Für Ihr<br><span class="dark-head">Unternehmen</span></div>
    <div class="abs tiny" style="left:210px;top:198px;width:150px">Beim Sicherheitsmanagement gibt es kein Pardon! Wer hier nicht ständig auf dem aktuellen Stand der Technik ist, begibt sich leicht in Gefahr. Und die Wiederherstellung verloren gegangener Daten ist nicht nur zeitaufwendig, sondern kann auch kostenintensiv werden.</div>
    <div class="abs bold" style="left:195px;top:292px;font-size:7px">Full-Service Dienstleister</div>
    <div class="abs tiny" style="left:195px;top:303px;width:165px">Mit unserem ganzheitlichen Lösungs- und Beratung unterstützen wir Ihr Unternehmen bei der Auswahl, Einführung, Entwicklung und dem Betrieb zeitgemäßer IT-Lösungen. Setzen Sie bei Ihrer Serverinfrastruktur auf führende Innovationen, um Bedrohungen zu verhindern.</div>
  </div>

  <div class="panel p3">
    <svg class="bg" viewBox="0 0 380 380">
      <rect x="0" y="50" width="70" height="130" fill="#e3e3e3" role="img" aria-label="Illustration: Figur lehnt an einem Laptop"/>
      <rect x="70" y="110" width="85" height="65" fill="#d2d2d2" role="img" aria-label="Illustration: aufgeklappter Laptop"/>
      <polygon points="215,55 370,40 370,120 205,140" fill="var(--blue)"/>
      <line x1="0" y1="180" x2="205" y2="140" stroke="var(--blue)" stroke-width="1.2"/>
      <line x1="150" y1="172" x2="370" y2="125" stroke="var(--blue)" stroke-width="1"/>
    </svg>
    <div class="abs" style="left:75px;top:48px;font-size:17px;line-height:.95;color:var(--blue);text-transform:uppercase">Noch<br>Fragen?</div>
    <div class="abs" style="left:228px;top:80px;font-size:17px;line-height:.95;color:#fff;text-transform:uppercase">Wir sind<br>für Sie da!</div>
    <div class="abs bold" style="left:80px;top:188px;font-size:7px">IT-Securitylösungen</div>
    <div class="abs tiny" style="left:80px;top:198px;width:285px">Ein Full-Service Dienstleister, der Lösungen für die heutigen Anforderungen an kleine und mittlere Unternehmen sowie Privatpersonen im IT-Bereich bereithält.</div>

    <svg class="icon" style="left:10px;top:255px" viewBox="0 0 24 24" fill="none" stroke="var(--blue)" stroke-width="1.6"><circle cx="12" cy="12" r="3.5"/><path d="M12 2v3M12 19v3M2 12h3M19 12h3M4.9 4.9l2.1 2.1M17 17l2.1 2.1M4.9 19.1L7 17M17 7l2.1-2.1"/><circle cx="12" cy="12" r="7"/></svg>
    <div class="abs bold" style="left:42px;top:240px;font-size:7px">Service</div>
    <div class="abs tiny" style="left:42px;top:251px;width:125px">Einrichten von DSL- und WLAN Vor-Ort Hilfe &amp; Konfiguration von Internetanschlüssen, Tausch von Hard- &amp; Software um Performance auf alten Systemen zu erhöhen.</div>

    <svg class="icon" style="left:10px;top:318px" viewBox="0 0 24 24" fill="none" stroke="var(--blue)" stroke-width="1.6"><rect x="5" y="10" width="14" height="11" rx="1.5"/><path d="M8 10V7a4 4 0 0 1 8 0v3"/><circle cx="12" cy="15" r="1.3"/></svg>
    <div class="abs bold" style="left:42px;top:306px;font-size:7px">Datenübernahme</div>
    <div class="abs tiny" style="left:42px;top:317px;width:125px">Sicherung vorhandener Daten auf externe Hardware. Rettung verloren gegangener Daten bei Hard- &amp; Software Defekt.</div>

    <svg class="icon" style="left:175px;top:255px" viewBox="0 0 24 24" fill="none" stroke="var(--blue)" stroke-width="1.6"><path d="M4 20l1-4L16 5l3 3L8 19z"/><path d="M3 9V4h8"/><path d="M21 13v8H8"/></svg>
    <div class="abs bold" style="left:208px;top:236px;font-size:7px">Installation</div>
    <div class="abs tiny" style="left:208px;top:247px;width:150px">Neuinstallation des Betriebssystems, Installation von Betriebssystemen, Treiberinstallation und individuell gewünschter Software.</div>

    <svg class="icon" style="left:175px;top:318px" viewBox="0 0 24 24" fill="none" stroke="var(--blue)" stroke-width="1.6"><rect x="3" y="6" width="18" height="13" rx="1.5"/><path d="M3 7l9 6 9-6"/></svg>
    <div class="abs bold" style="left:208px;top:306px;font-size:7px">E-Mail Service</div>
    <div class="abs tiny" style="left:208px;top:317px;width:150px">Hilfe bei Problemen mit E-Mail-Programmen und Providern, und bei vielen weiteren IT &amp; EDV Problemen einfach nachfragen.</div>
  </div>
</div>
<div class="caption" style="top:2460px">Flyer Innen geöffnet</div>

</body>
</html>
```